Création de la plaquette commerciale de la VTR
Besoins
Nous avons besoin d'une plaquette commerciale décrivant l'ensemble des activités de notre entreprise tout en montrant notre dynamisme, notre professionnalisme et disponibilité.
Description de l'entreprise
La V.T.R. est une société de services en ingénierie informatique dont les activités sont :
. INGÉNIERIE : Audit des systèmes d'information, Conseil en informatique et système d'information, Ingénierie informatique (conception, développement, fabrication de système d'information
. INTERNET : Conception et design de site web, hébergement internet
. VAR : Revendeur à valeur ajoutée (matériels, logiciels, périphériques, consommables, ...)
. MAINTENANCE : Maintenance sur site avec contrat
Notre site internet :
www.vtr-lomapo.net
La cible
Notre cible est l'ensemble des professionnels et plus particulièrement les TPE, PME & PMI
Couleurs, favoris et autres exigences:
Notre besoin est :
. une plaquette commerciale au format A3 plié en 2 pour les 4 activités
. des feuillets pour les références ingénierie, web, sociétés

```html
<!DOCTYPE html>
<html lang="fr">
<head>
<meta charset="utf-8">
<title>V.T.R. — Plaquette commerciale</title>
<link href="https://fonts.googleapis.com/css2?family=Arimo:wght@400;700&display=swap" rel="stylesheet">
<style>
  :root{
    --green:#78c394;
    --yellow:#f6e07c;
    --lavender:#a9bee6;
    --bar:#4e8fe2;
    --accent:#3f86e8;
    --white:#ffffff;
    --grey:#8c8a7c;
    --rule:rgba(255,255,255,.55);
  }
  *{margin:0;padding:0;box-sizing:border-box}
  html,body{width:1200px;height:857px;overflow:hidden;background:#fff}
  body{font-family:"Arimo",Arial,sans-serif;color:var(--white)}
  .brochure{position:relative;width:1200px;height:857px;background:var(--lavender)}
  .band{position:absolute}
  .band--green-left{left:0;top:0;width:584px;height:250px;background:var(--green)}
  .band--green-right{left:612px;top:0;width:588px;height:250px;background:var(--green)}
  .band--yellow-left{left:0;top:250px;width:584px;height:166px;background:var(--yellow)}
  .band--yellow-right{left:612px;top:250px;width:588px;height:166px;background:var(--yellow)}
  .bar-vertical{position:absolute;left:584px;top:0;width:28px;height:857px;background:var(--bar)}
  .bar-horizontal{position:absolute;left:0;top:416px;width:1200px;height:24px;background:var(--bar)}

  .intro{position:absolute;left:32px;top:20px;width:530px;font-size:18px;line-height:23px}
  .brand{color:var(--accent)}
  .section-title{position:absolute;font-size:18px;font-weight:400;padding-bottom:8px;border-bottom:1px solid var(--rule)}
  .section-title--ingenierie{left:30px;top:100px;width:530px}
  .section-title--var{left:630px;top:100px;width:540px}
  .section-title--internet{left:30px;top:616px;width:530px}
  .section-title--maintenance{left:630px;top:616px;width:540px}

  .copy{position:absolute;font-size:11.5px;line-height:14px}
  .copy--muted{color:var(--grey);border-top:1px solid rgba(255,255,255,.7);padding-top:10px}
  .copy--ing{left:30px;top:150px;width:525px}
  .copy--ing-2{left:30px;top:256px;width:525px}
  .copy--var{left:630px;top:150px;width:540px}
  .copy--var-2{left:630px;top:256px;width:540px}
  .copy--web{left:30px;top:670px;width:525px;font-size:12px;line-height:15px}
  .copy--maint{left:630px;top:670px;width:540px;font-size:12px}
  .brand-lg{color:var(--accent);font-size:17px}
  .tech{color:var(--accent);font-size:17px}
  .copy--web p+p{margin-top:8px}

  .photo{position:absolute;border:2px solid #fff}
  .photo--office{left:486px;top:336px;width:96px;height:64px;background:linear-gradient(160deg,#3d6fb0,#8fb6d8 55%,#d9c36a)}
  .photo--screen{left:420px;top:448px;width:104px;height:68px;background:linear-gradient(160deg,#5a7fb8,#d7e2ee 55%,#7fa3c8)}
  .photo--workshop{left:616px;top:448px;width:104px;height:68px;background:linear-gradient(160deg,#c9ccd4,#f1f1f1 50%,#b43a3a)}
</style>
</head>
<body>
<main class="brochure">
  <div class="band band--green-left"></div>
  <div class="band band--green-right"></div>
  <div class="band band--yellow-left"></div>
  <div class="band band--yellow-right"></div>
  <div class="bar-vertical"></div>
  <div class="bar-horizontal"></div>

  <p class="intro">&nbsp;La <span class="brand">V.T.R.</span> est une société de services en ingénierie informatique dont les activités sont :</p>

  <h2 class="section-title section-title--ingenierie">Ingénerie</h2>
  <div class="copy copy--ing">
    <p>Audit des systèmes d'information. Conseil en informatique et système d'information, Ingénierie informatique (conception, développement, fabrication de système d'information).</p>
    <p>Le service d'audit de parc informatique : analyser et inventorier le fonctionnement du système d'information en couvrant généralement les postes de travail fixes et mobiles, les serveurs et leurs rôles au sein du système, le moyens de connexion à internet, également l'analyse d'infrastructure système et réseau ainsi que la sécurité informatique.</p>
  </div>
  <div class="copy copy--muted copy--ing-2">
    <p>L'informatique est une technologie en perpétuelle évolution. A l'heure de faire un choix (de matériel, de fournisseur d'accès...), il est difficile pour le non initié de s'y retrouver. Nos prestations de conseil sont là pour vous y aider. A partir de l'étude de vos besoins et de votre budget nous vous orientons vers la solution la mieux adaptée.</p>
  </div>
  <div class="photo photo--office" role="img" aria-label="Photo d'un bureau équipé de postes informatiques"></div>

  <h2 class="section-title section-title--var">VAR</h2>
  <div class="copy copy--var">
    <p><span class="brand-lg">VAR</span>, acronyme de l'anglais Value-added Reseller, désigne un revendeur (généralement informatique) à valeur ajoutée. Par valeur ajoutée, on entend le fait qu'il exerce un métier de revente, mais aussi une activité de service.</p>
    <p>Par exemple, une entreprise peut acheter une unité centrale d'ordinateur à un fournisseur donné, un périphérique d'impression de haute qualité à un autre et un éditeur d'image matricielle.</p>
  </div>
  <div class="copy copy--muted copy--var-2">
    <p>L'entreprise paramètre ensuite le tout pour en faire un système dédié à la conception assistée par ordinateur. En assemblant les différents éléments choisis, elle aura ajouté de la valeur à l'ensemble en réalisant un système haut de gamme dédié à une fonction spécialisée.</p>
  </div>

  <div class="photo photo--screen" role="img" aria-label="Capture d'écran d'une application de gestion"></div>
  <div class="photo photo--workshop" role="img" aria-label="Photo d'un atelier de maintenance avec un véhicule"></div>

  <h2 class="section-title section-title--internet">Internet</h2>
  <div class="copy copy--web">
    <p><span class="brand-lg">V.T.R.</span> réalise et développe vos projet web sur mesure pour augmenter votre présence sur le web et pour valoriser votre image de marque avec des créations de hautes qualités. En tant qu'agence spécialisée, nous veillons au respect de délai et de qualité de notre produit final.</p>
    <p>Nous sommes compétents dans plusieurs languages de programmation : <span class="tech">PHP, HTML, CSS, KOVA</span> et plusieurs technologies web : <span class="tech">TRAMIO !, WEBLIZ, HEBRANO..</span></p>
  </div>

  <h2 class="section-title section-title--maintenance">Maintenance</h2>
  <div class="copy copy--maint">
    <p><span class="brand-lg">V.T.R.</span> assure aussi la maintenance de votre web, grâce à une équipe d'assistance.</p>
  </div>
</main>
</body>
</html>
```